Mobile Fitness snd Therapy Business Card Design

I need a business card designed for my mobile fitness and therapy business.

Please view the images that I have uploaded. I like the simplicity of the design that I have attached. I adapted it with my information

Target Market(s)

Those seeking personal training, injury rehabilitation or massage therapy.

Industry/Entity Type

Business

Contact Information for Business Card

Dylan Marwick - MSc, CAT(C), RMT, CSCS, Pn2
e-mail: dylan@vantrelo.com
website: www.vantrelo.com
instagram: @dylan_marwick

Font styles to use
Sans Serif

Colors
3176b5
0355a3

Requirements
Must have
• "Contact us to receive a FREE assessment"
• Services offered:
• Personal Training
• Golf Fitness
• Injury Rehab
• Massage Therapy
• Yoga
Nice to have
• Consistent colours with brand
• - Dark Blue: #232837
• - Blue: #5096f0
• Consistent look/feel with the website: www.vantrelo.com

```html
<!DOCTYPE html>
<html lang="en">
<head>
<meta charset="UTF-8">
<title>Vantrelo Business Card</title>
<link href="https://fonts.googleapis.com/css2?family=Raleway:wght@400;500;700;800&family=Saira:wght@600;700&display=swap" rel="stylesheet">
<style>
  :root {
    --backdrop: #ecebe7;
    --card-black: #050505;
    --card-white: #f6f6f4;
    --ink: #1d1f24;
    --ink-soft: #4a4d55;
    --white: #ffffff;
    --blue-light: #6fa8e4;
    --blue: #3176b5;
    --blue-deep: #3265c4;
    --pill: #e4e5e8;
  }
  * { margin: 0; padding: 0; box-sizing: border-box; }
  html, body { width: 1200px; height: 800px; overflow: hidden; }
  body { background: var(--backdrop); position: relative; font-family: "Raleway", sans-serif; }

  .card {
    position: absolute;
    top: 252px;
    width: 520px;
    height: 297px;
    border-radius: 4px;
    overflow: hidden;
    box-shadow: 0 6px 18px rgba(0,0,0,0.18);
  }

  /* Front */
  .card-front { left: 50px; background: var(--card-black); color: var(--white); }
  .brand {
    position: absolute;
    left: 0; right: 0; top: 92px;
    text-align: center;
  }
  .brand-name {
    font-family: "Saira", sans-serif;
    font-weight: 700;
    font-size: 56px;
    letter-spacing: 4px;
    line-height: 1;
    color: var(--white);
  }
  .brand-tagline {
    margin-top: 10px;
    font-weight: 800;
    font-size: 14px;
    letter-spacing: 3px;
    color: var(--white);
  }
  .services {
    position: absolute;
    left: 22px; right: 22px; bottom: 22px;
    font-size: 11.5px;
    font-weight: 500;
    letter-spacing: 0.2px;
    color: var(--white);
    white-space: nowrap;
  }

  /* Back */
  .card-back { left: 630px; background: var(--card-white); color: var(--ink); }
  .tab-left {
    position: absolute;
    left: 0; top: 70px;
    width: 16px; height: 190px;
    background: var(--blue-light);
    border-radius: 0 14px 14px 0;
  }
  .tab-right {
    position: absolute;
    right: 0; top: 150px;
    width: 20px; height: 160px;
    background: var(--blue-deep);
    border-radius: 14px 0 0 14px;
  }
  .holder {
    position: absolute;
    left: 40px; top: 112px;
  }
  .holder-name {
    font-family: "Saira", sans-serif;
    font-weight: 700;
    font-size: 23px;
    letter-spacing: 0.5px;
    line-height: 1.05;
    color: var(--ink);
  }
  .holder-credentials {
    margin-top: 2px;
    font-size: 12px;
    font-weight: 500;
    color: var(--ink-soft);
  }
  .divider-pill {
    position: absolute;
    left: 262px; top: 46px;
    width: 32px; height: 176px;
    background: var(--pill);
    border-radius: 16px;
  }
  .divider-pill::after {
    content: "";
    position: absolute;
    left: 15px; top: 52px;
    width: 2px; height: 72px;
    background: var(--ink);
  }
  .contacts {
    position: absolute;
    left: 314px; top: 102px;
    list-style: none;
  }
  .contacts li {
    display: flex;
    align-items: center;
    gap: 9px;
    font-size: 13.5px;
    font-weight: 500;
    color: var(--ink);
    height: 21px;
  }
  .contacts svg { width: 13px; height: 13px; flex: none; }
  .offer {
    position: absolute;
    left: 0; right: 0; bottom: 28px;
    text-align: center;
    font-size: 13px;
    font-weight: 500;
    color: var(--ink);
  }
  .offer strong { color: var(--blue); font-weight: 800; }
</style>
</head>
<body>

  <section class="card card-front">
    <div class="brand">
      <div class="brand-name">VANTRELO</div>
      <div class="brand-tagline">NUTRITION - FITNESS - HEALTH</div>
    </div>
    <p class="services">Personal Training | Golf Fitness | Injury Rehab | Massage Therapy | Yoga</p>
  </section>

  <section class="card card-back">
    <div class="tab-left"></div>
    <div class="tab-right"></div>

    <div class="holder">
      <h1 class="holder-name">DYLAN MARWICK</h1>
      <p class="holder-credentials">MSc, CAT(C), RMT, CSCS, Pn2</p>
    </div>

    <div class="divider-pill"></div>

    <ul class="contacts">
      <li>
        <svg viewBox="0 0 16 16"><path fill="#3176b5" d="M3.6 1.2l2.3 2.6-1.2 1.8c.8 1.9 2.2 3.3 4.1 4.1l1.8-1.2 2.6 2.3-1.2 2.4C7.2 13.5 2.5 8.8 1.2 3.9z"/></svg>
        <span>250-555-0147</span>
      </li>
      <li>
        <svg viewBox="0 0 16 16"><rect x="1" y="3" width="14" height="10" rx="1" fill="#3176b5"/><path d="M1.5 3.8L8 8.8l6.5-5" fill="none" stroke="#f6f6f4" stroke-width="1.3"/></svg>
        <span>dylan@vantrelo.com</span>
      </li>
      <li>
        <svg viewBox="0 0 16 16"><g fill="none" stroke="#3176b5" stroke-width="1.4"><circle cx="8" cy="8" r="6.5"/><ellipse cx="8" cy="8" rx="2.8" ry="6.5"/><path d="M1.5 8h13"/></g></svg>
        <span>www.vantrelo.com</span>
      </li>
      <li>
        <svg viewBox="0 0 16 16"><rect x="1.5" y="1.5" width="13" height="13" rx="3" fill="#3176b5"/></svg>
        <span>@dylan_marwick</span>
      </li>
    </ul>

    <p class="offer">Contact us to receive a <strong>FREE</strong> assessment</p>
  </section>

</body>
</html>
```